KB Rubbish Removal Business Card

Hey,
I need a double sided business card designed for a rubbish removal business based in Australia. Logo is already chosen, similar colours preferred for both sides of the business card.

Details to include:

Front:

KB Rubbish Removal
Darren Holloway
Managing Director
Mobile: 0471 902 146
Email: darren@kbrubbishremoval.com.au
Website: kbrubbishremoval.com.au

Rear:

How did we do?
kbrubbishremoval.com.au/review

```html
<!DOCTYPE html>
<html lang="en">
<head>
<meta charset="utf-8">
<title>KB Rubbish Removal – Business Card</title>
<link rel="stylesheet" href="https://fonts.googleapis.com/css2?family=Alegreya+Sans:wght@400;500;700&display=swap">
<style>
  :root {
    --page: #e4e6e4;
    --card: #ffffff;
    --green-dark: #1f7a3a;
    --green: #3a9a4a;
    --lime: #8cc63f;
    --leaf-a: #8fc9a0;
    --leaf-b: #b5dca0;
    --grey: #6b6b6b;
    --grey-dark: #4a4a4a;
    --photo-a: #8a6a52;
    --photo-b: #c9c2b4;
  }
  * { box-sizing: border-box; margin: 0; padding: 0; }
  html, body { width: 1200px; height: 900px; overflow: hidden; }
  body {
    background: var(--page);
    font-family: "Alegreya Sans", sans-serif;
    position: relative;
  }
  .card {
    position: absolute;
    left: 250px;
    width: 700px;
    height: 400px;
    background: linear-gradient(135deg, #ffffff 0%, #f1f2f1 100%);
    box-shadow: 0 6px 18px rgba(0,0,0,0.18);
    overflow: hidden;
  }
  .card--back { top: 30px; }
  .card--front { top: 470px; }

  /* decoration areas: soft tint fields */
  .decor {
    position: absolute;
    background: linear-gradient(135deg, var(--leaf-b) 0%, var(--leaf-a) 100%);
    opacity: 0.55;
  }
  .card--back .decor--top { left: 0; top: 30px; width: 240px; height: 65px; }
  .card--back .decor--bottom { left: 160px; top: 240px; width: 120px; height: 160px; }
  .card--front .decor--top { right: 10px; top: 0; width: 150px; height: 170px; }
  .card--front .decor--bottom { right: 0; top: 235px; width: 270px; height: 95px; }

  /* brand mark */
  .brand { position: absolute; display: flex; align-items: center; gap: 12px; }
  .brand__dot { width: 34px; height: 34px; border-radius: 50%; background: var(--green); flex: none; }
  .brand__name { font-weight: 500; color: var(--grey-dark); font-size: 26px; letter-spacing: 0.5px; white-space: nowrap; }
  .card--back .brand { top: 28px; right: 30px; }
  .card--back .brand__dot { width: 24px; height: 24px; }
  .card--back .brand__name { font-size: 17px; }
  .card--front .brand { top: 70px; left: 48px; }

  /* back */
  .review { position: absolute; right: 30px; top: 100px; text-align: right; }
  .review__title { color: var(--green-dark); font-weight: 700; font-size: 24px; }
  .review__url { color: var(--grey); font-size: 22px; margin-top: 4px; }
  .compare { position: absolute; right: 25px; top: 200px; display: flex; gap: 18px; }
  .compare__item { width: 172px; }
  .compare__label { color: var(--green-dark); font-weight: 700; font-size: 19px; margin-bottom: 6px; }
  .compare__photo { width: 172px; height: 126px; border: 3px solid var(--lime); }
  .compare__photo--before { background: linear-gradient(160deg, #4f6e3c 0%, var(--photo-b) 45%, var(--photo-a) 100%); }
  .compare__photo--after { background: linear-gradient(170deg, var(--photo-b) 0%, #d8d2c6 45%, var(--photo-a) 100%); }

  /* front */
  .person { position: absolute; left: 48px; top: 165px; }
  .person__name { color: var(--green); font-weight: 500; font-size: 30px; letter-spacing: 1px; text-transform: uppercase; }
  .person__role { color: var(--grey); font-size: 21px; margin-top: 2px; }
  .contacts { position: absolute; left: 48px; top: 262px; list-style: none; }
  .contacts li { display: flex; align-items: center; gap: 10px; color: var(--grey); font-size: 21px; line-height: 34px; }
  .contacts svg { width: 16px; height: 16px; flex: none; }
</style>
</head>
<body>

<section class="card card--back" aria-label="Business card rear">
  <div class="decor decor--top" role="img" aria-label="Decorative green leaf shapes"></div>
  <div class="decor decor--bottom" role="img" aria-label="Decorative green leaf shape"></div>

  <div class="brand">
    <span class="brand__dot"></span>
    <span class="brand__name">KB Rubbish Removal</span>
  </div>

  <div class="review">
    <p class="review__title">How did we do?</p>
    <p class="review__url">kbrubbishremoval.com.au/review</p>
  </div>

  <div class="compare">
    <figure class="compare__item">
      <figcaption class="compare__label">Before</figcaption>
      <div class="compare__photo compare__photo--before" role="img" aria-label="Photo of a cluttered side path with rubbish bags before removal"></div>
    </figure>
    <figure class="compare__item">
      <figcaption class="compare__label">After</figcaption>
      <div class="compare__photo compare__photo--after" role="img" aria-label="Photo of the same side path swept clean after removal"></div>
    </figure>
  </div>
</section>

<section class="card card--front" aria-label="Business card front">
  <div class="decor decor--top" role="img" aria-label="Decorative green leaf shape"></div>
  <div class="decor decor--bottom" role="img" aria-label="Decorative green leaf shapes"></div>

  <div class="brand">
    <span class="brand__dot"></span>
    <span class="brand__name">KB Rubbish Removal</span>
  </div>

  <div class="person">
    <p class="person__name">Darren Holloway</p>
    <p class="person__role">Managing Director</p>
  </div>

  <ul class="contacts">
    <li>
      <svg viewBox="0 0 16 16" aria-hidden="true"><rect x="4" y="1" width="8" height="14" rx="1.5" fill="none" stroke="var(--green)" stroke-width="1.6"/><circle cx="8" cy="12.5" r="0.9" fill="var(--green)"/></svg>
      0471 902 146
    </li>
    <li>
      <svg viewBox="0 0 16 16" aria-hidden="true"><rect x="1" y="3" width="14" height="10" rx="1.5" fill="var(--green)"/><path d="M1.5 4 L8 9 L14.5 4" fill="none" stroke="#fff" stroke-width="1.3"/></svg>
      darren@kbrubbishremoval.com.au
    </li>
    <li>
      <svg viewBox="0 0 16 16" aria-hidden="true"><circle cx="8" cy="8" r="7" fill="var(--green)"/></svg>
      kbrubbishremoval.com.au
    </li>
  </ul>
</section>

</body>
</html>
```